Harbor Networks Pty Ltd

We are a Sydney based IT services company, providing managed services for corporate clients, established for over 10 years. Amongst our services we provide full infrastructure support, maintenance and upgrades. We also provide helpdesk/remote support and cloud services.

We were hoping to keep our original colours and our logo (Blue and Green, please visit our website www.harbornetworks-demo.com.au) however we are looking for a new business card design (with better resolution and finish) with multiple variation of the blue and green colour design options. Happy for alternative suggestion. ie new blue and green / grey and green / blue and grey et and please feel free to update current logo size ie large or smaller. (Attached our current logo and business card desig)

Business

Contact Information for Business Card

Name, Title, Address, Contract Information, Company Name and Logo.
(QR code if possible)

Colors
0455a3
33a6d7
3276b5
85acd3
85cae6
9bcb3c
add136
cadf82
e9f1ce

```html
<!DOCTYPE html>
<html lang="en">
<head>
<meta charset="utf-8">
<title>Harbor Networks – Business Card</title>
<link rel="stylesheet" href="https://fonts.googleapis.com/css2?family=Open+Sans:wght@300;400;600&display=swap">
<style>
  :root {
    --blue-deep: #0455a3;
    --blue-mid: #3276b5;
    --green: #9bcb3c;
    --ink: #2e2e2e;
    --rule: #c9c9c9;
    --card-top: #ffffff;
    --card-bottom: #e6e7e8;
    --backdrop: #d6d7d9;
    --watermark: #dcdcdc;
  }
  * { box-sizing: border-box; margin: 0; padding: 0; }
  html, body { width: 1200px; height: 900px; overflow: hidden; }
  body {
    background: var(--backdrop);
    font-family: "Open Sans", Arial, sans-serif;
    color: var(--ink);
    position: relative;
  }
  .card {
    position: absolute;
    left: 290px;
    width: 620px;
    height: 354px;
    background: radial-gradient(ellipse at 40% 30%, var(--card-top) 0%, #f4f4f5 45%, var(--card-bottom) 100%);
    box-shadow: 0 6px 18px rgba(0,0,0,0.18);
    overflow: hidden;
  }
  .card--front { top: 62px; }
  .card--back { top: 484px; }

  .wordmark {
    font-weight: 300;
    color: var(--blue-deep);
    letter-spacing: -0.5px;
    white-space: nowrap;
  }

  /* front */
  .front__brand {
    position: absolute; top: 92px; left: 0; right: 0;
    display: flex; flex-direction: column; align-items: center;
  }
  .front__brand .wordmark { font-size: 44px; }
  .front__tagline { margin-top: 6px; font-size: 14px; color: var(--green); }
  .front__services {
    position: absolute; left: 48px; right: 40px; bottom: 44px;
    display: flex; justify-content: space-between;
  }
  .service-group { list-style: none; }
  .service-group li {
    font-size: 11.5px; line-height: 1.45; color: var(--ink);
    padding-left: 9px; position: relative; white-space: nowrap;
  }
  .service-group li::before {
    content: ""; position: absolute; left: 0; top: 8px;
    width: 5px; height: 2px; background: var(--blue-mid);
  }

  /* back */
  .back__glow {
    position: absolute; right: 0; top: 0; width: 330px; height: 354px;
    background: radial-gradient(ellipse at 70% 40%, var(--watermark) 0%, rgba(220,220,220,0) 70%);
  }
  .back__brand { position: absolute; left: 40px; top: 118px; }
  .back__brand .wordmark { font-size: 32px; }
  .person {
    position: absolute; left: 352px; top: 48px;
    padding-left: 14px; border-left: 1px solid var(--rule);
  }
  .person__name { font-size: 22px; font-weight: 400; color: var(--ink); }
  .person__title { font-size: 12px; white-space: nowrap; }
  .tone-green { color: var(--green); }
  .tone-blue { color: var(--blue-mid); }
  .contact {
    position: absolute; top: 196px;
    padding-left: 12px; border-left: 1px solid var(--rule);
    font-size: 11px; line-height: 1.5; white-space: nowrap;
  }
  .contact--phones { left: 206px; }
  .contact--online { left: 360px; }
  .contact dt { display: inline; }
  .contact dd { display: inline; color: var(--ink); }
  .contact .line { display: block; }
  .contact .block { margin-bottom: 12px; }
  .contact .block:last-child { margin-bottom: 0; }
  .company {
    position: absolute; left: 40px; top: 244px;
    font-size: 11px; line-height: 1.5; color: var(--ink);
    font-style: normal; white-space: nowrap;
  }
  .company__name { color: var(--green); }
  .company__web { color: var(--blue-mid); margin-top: 10px; }
</style>
</head>
<body>

  <section class="card card--front" aria-label="Business card front">
    <div class="front__brand">
      <div class="wordmark">harbornetworks</div>
      <p class="front__tagline">Managed IT Support Is Our Business</p>
    </div>
    <div class="front__services">
      <ul class="service-group">
        <li>Quality IT Support and Advice</li>
        <li>Fixed Fee Support and Projects</li>
      </ul>
      <ul class="service-group">
        <li>Competitive Rates</li>
        <li>Over 10 Years Experience</li>
      </ul>
      <ul class="service-group">
        <li>No Ties Support Agreements</li>
        <li>Tailored Support Solutions</li>
      </ul>
    </div>
  </section>

  <section class="card card--back" aria-label="Business card back">
    <div class="back__glow"></div>
    <div class="back__brand">
      <div class="wordmark">harbornetworks</div>
    </div>
    <div class="person">
      <p class="person__name">Dana Keller</p>
      <p class="person__title"><span class="tone-green">Director</span> / <span class="tone-blue">Managed IT Services</span></p>
    </div>
    <dl class="contact contact--phones">
      <div class="block">
        <span class="line"><dt class="tone-green">tel: </dt><dd>1300 555 010</dd></span>
        <span class="line"><dt class="tone-green">direct: </dt><dd>+61 2 5550 1234</dd></span>
      </div>
      <div class="block">
        <span class="line"><dt class="tone-blue">fax: </dt><dd>+61 2 5550 5678</dd></span>
        <span class="line"><dt class="tone-blue">mob: </dt><dd>+61 400 555 019</dd></span>
      </div>
    </dl>
    <dl class="contact contact--online">
      <div class="block">
        <span class="line"><dt class="tone-green">helpdesk:</dt></span>
        <span class="line"><dd>service@harbornetworks-demo.com.au</dd></span>
      </div>
      <div class="block">
        <span class="line"><dt class="tone-blue">email:</dt></span>
        <span class="line"><dd>dana.keller@harbornetworks-demo.com.au</dd></span>
      </div>
    </dl>
    <address class="company">
      <p class="company__name">Harbor Networks Pty Ltd</p>
      <p>Level 4, 18 Sample Street</p>
      <p>Sydney, NSW 2000 Australia</p>
      <p class="company__web">www.harbornetworks-demo.com.au</p>
    </address>
  </section>

</body>
</html>
```